General Power Point Presentation Pack

Hello Designers,

I am after a professional looking Microsoft PowerPoint deck that can be used for our corporate presentations. The pack should include a:

Title Page
Tittle and Content Page
Section Header Sheet
Two Content Page
Title Only Page
Blank Page
Content with Caption Page
Picture with Caption Page

I have included my brand guidelines and colours. I have also included some photos you may be able to use. Can you please ensure the pack has page numbering and that when you print it that it can be printed to full A4 Page.

Industry/Entity Type

Property Development & Construction

Requirements
Must have
• Prefer a white or very light coloured background

```html
<!DOCTYPE html>
<html lang="en">
<head>
<meta charset="utf-8">
<title>Ardenholt – PowerPoint Presentations</title>
<link href="https://fonts.googleapis.com/css2?family=Roboto:wght@400;500;700;900&display=swap" rel="stylesheet">
<style>
  :root{
    --bg:#ececec;
    --white:#ffffff;
    --orange:#ef9f5a;
    --orange-deep:#de7a4a;
    --brand:#c94f1d;
    --beige:#f1ead9;
    --ink:#3d3d3d;
    --muted:#8a8a8a;
    --photo:linear-gradient(180deg,#a9c0d6 0%,#c7d3dc 30%,#8a6a55 55%,#6e4a38 78%,#6f7f4f 100%);
  }
  *{box-sizing:border-box;margin:0;padding:0}
  html,body{width:1048px;height:1200px;overflow:hidden}
  body{background:var(--bg);font-family:"Roboto",Arial,sans-serif;color:var(--ink);position:relative}

  .hero{position:absolute;left:44px;top:31px;width:961px;height:267px;background:var(--white)}
  .hero-brand{position:absolute;left:0;width:100%;top:170px;text-align:center;font-weight:500;font-size:46px;line-height:1;color:var(--brand);letter-spacing:1px}

  .pack-title{position:absolute;left:0;width:1048px;top:322px;text-align:center;font-size:22px;font-weight:400;color:#8d8d8d}
  .pack-rule{position:absolute;left:480px;top:367px;width:85px;height:3px;background:var(--orange)}

  .slide{position:absolute;width:303px;height:170px;background:var(--white);overflow:hidden}
  .col1{left:44px}.col2{left:373px}.col3{left:701px}
  .row1{top:408px}.row2{top:601px}.row3{top:794px}.row4{top:985px}

  .brand-tag{position:absolute;right:16px;top:15px;font-size:8px;font-weight:500;color:var(--orange);display:flex;align-items:center;gap:2px}
  .brand-tag .mark{width:5px;height:6px;background:currentColor}
  .brand-tag.light{color:var(--white)}
  .base-line{position:absolute;left:0;bottom:0;width:228px;height:2px;background:var(--orange)}
  .page-no{position:absolute;right:8px;bottom:5px;font-size:3.5px;color:var(--muted)}

  .s-title{position:absolute;font-size:10px;font-weight:500;color:var(--ink);line-height:1.2}
  .s-rule{position:absolute;width:13px;height:2px;background:var(--orange)}
  .body{position:absolute;font-size:3.4px;line-height:1.5;color:#555}
  .body p+p{margin-top:3px}
  .photo{position:absolute;background:var(--photo)}

  .title-strip{position:absolute;left:0;top:36px;width:14px;height:98px;background:var(--beige)}
  .title-photo{left:104px;top:0;width:199px;height:170px}
  .title-card{position:absolute;left:28px;top:36px;width:177px;height:98px;background:var(--orange-deep);opacity:.94;color:var(--white);text-align:center;padding-top:42px}
  .title-card .name{font-size:14px;font-weight:500}
  .title-card .sub{font-size:7px;letter-spacing:1.6px;margin-top:3px}
  .play{position:absolute;left:195px;top:75px;width:21px;height:21px}

  .sec-bar{position:absolute;left:18px;top:0;width:7px;height:43px;background:var(--orange)}
  .sec-block{position:absolute;left:0;top:36px;width:73px;height:99px;background:var(--beige)}
  .sec-tab{position:absolute;left:66px;top:46px;width:46px;height:5px;background:var(--orange)}
  .sec-title{position:absolute;left:33px;top:58px;font-size:19px;font-weight:700;color:#555;line-height:1.05}
  .sec-note{position:absolute;left:33px;top:103px;width:200px;font-size:3.4px;line-height:1.4;color:#999}
  .sec-line{position:absolute;left:235px;top:116px;width:55px;height:2px;background:var(--orange)}
  .sec-dark{position:absolute;left:0;top:135px;width:46px;height:2px;background:var(--orange-deep)}

  .tc-panel{position:absolute;left:0;top:0;width:115px;height:170px;background:var(--orange);color:var(--white)}
  .tc-panel .s-title{color:var(--white);left:14px;top:14px}
  .tc-panel .s-rule{background:var(--white);left:14px;top:40px}
  .tc-panel .body{color:var(--white);left:14px;top:48px;width:90px}
  .tc-box{position:absolute;left:105px;top:40px;width:172px;height:114px;background:var(--beige)}
  .tc-box .s-title{left:21px;top:11px}
  .tc-box .s-rule{left:21px;top:36px}
  .tc-box .body{left:21px;top:48px;width:140px}

  .cc-photo{left:0;top:0;width:88px;height:170px;background:linear-gradient(180deg,#ece6da,#e3d9c6 60%,#d8cdb8);opacity:.9}
  .num{position:absolute;left:82px;width:14px;height:14px;border-radius:50%;background:var(--white);border:1px solid var(--orange);font-size:5px;color:var(--orange);display:flex;align-items:center;justify-content:center;font-weight:500}
  .cc .s-title{font-size:7.5px;left:110px;color:var(--ink)}
  .cc .body{left:110px;width:180px}

  .pc-panel{position:absolute;left:132px;top:0;width:171px;height:170px;background:var(--orange)}
  .pc-photo{left:14px;top:52px;width:159px;height:79px}
  .pc .body{left:188px;top:53px;width:94px;color:var(--white)}
  .pc .base-line{width:132px}

  .tile{position:absolute;width:55px}
  .pg .s-title{left:128px;top:30px}
  .pg .s-rule{left:128px;top:58px}
  .pg .body{left:128px;top:67px;width:162px}

  .ty-photo{left:0;top:0;width:208px;height:170px}
  .ty-strip{position:absolute;left:290px;top:35px;width:13px;height:99px;background:var(--beige)}
  .ty-card{position:absolute;left:101px;top:35px;width:178px;height:99px;background:var(--orange-deep);opacity:.94;color:var(--white);text-align:center;padding-top:27px}
  .ty-card .big{font-size:24px;font-weight:700;line-height:1}
  .ty-card .rule{width:42px;height:1px;background:var(--white);margin:7px auto 6px}
  .ty-card .name{font-size:10px;font-weight:500}
</style>
</head>
<body>

<section class="hero">
  <div class="hero-brand">Ardenholt</div>
</section>

<h1 class="pack-title">PowerPoint Presentations</h1>
<div class="pack-rule"></div>

<article class="slide col1 row1">
  <div class="title-strip"></div>
  <div class="photo title-photo" role="img" aria-label="Photo of a modern brick apartment building"></div>
  <div class="title-card">
    <div class="name">Ardenholt</div>
    <div class="sub">PRESENTATION</div>
  </div>
  <svg class="play" viewBox="0 0 21 21"><circle cx="10.5" cy="10.5" r="10.5" fill="#fff"/><path d="M8.5 6.5 L14.5 10.5 L8.5 14.5 Z" fill="#de7a4a"/></svg>
</article>

<article class="slide col2 row1">
  <div class="s-title" style="left:14px;top:12px">Lorem ipsum dolor sit</div>
  <div class="s-rule" style="left:14px;top:28px"></div>
  <div class="brand-tag"><span class="mark"></span>Ardenholt</div>
  <div class="body" style="left:28px;top:38px;width:205px">
    <p>Lorem ipsum dolor sit amet, consectetuer adipiscing elit, sed diam nonummy nibh euismod tincidunt ut laoreet dolore magna aliquam erat volutpat. Ut wisi enim ad minim veniam, quis nostrud exerci tation ullamcorper suscipit lobortis nisl ut aliquip ex ea commodo consequat. Duis autem vel eum iriure dolor in hendrerit in vulputate velit esse molestie.</p>
    <p>Consequat, vel illum dolore eu feugiat nulla facilisis at vero eros et accumsan et iusto odio dignissim qui blandit praesent luptatum zzril delenit augue duis dolore te feugait nulla facilisi.</p>
    <p>Lorem ipsum dolor sit amet, consectetuer adipiscing elit, sed diam nonummy nibh euismod tincidunt ut laoreet dolore magna aliquam erat volutpat. Ut wisi enim ad minim veniam, quis nostrud exerci tation ullamcorper. Lorem ipsum dolor sit amet, consectetuer adipiscing elit, sed diam nonummy nibh euismod tincidunt ut laoreet dolore magna aliquam erat volutpat.</p>
    <p>Lorem ipsum dolor sit amet, consectetuer adipiscing elit, sed diam nonummy nibh euismod tincidunt ut laoreet dolore magna aliquam erat volutpat. Ut wisi enim ad minim veniam, quis nostrud exerci tation ullamcorper suscipit lobortis nisl.</p>
  </div>
  <div class="base-line"></div><div class="page-no">2</div>
</article>

<article class="slide col3 row1">
  <div class="sec-block"></div>
  <div class="sec-bar"></div>
  <div class="sec-tab"></div>
  <div class="brand-tag"><span class="mark"></span>Ardenholt</div>
  <div class="sec-title">SECTION HEADER<br>TITLE</div>
  <div class="sec-note">Lorem ipsum dolor sit amet, consectetuer adipiscing elit, sed diam nonummy nibh euismod tincidunt ut laoreet dolore magna aliquam erat volutpat. Ut wisi enim ad minim veniam, quis nostrud exerci tation.</div>
  <div class="sec-line"></div>
  <div class="sec-dark"></div>
  <div class="base-line"></div><div class="page-no">3</div>
</article>

<article class="slide col1 row2">
  <div class="tc-panel">
    <div class="s-title">Lorem ipsum<br>dolor sit</div>
    <div class="s-rule"></div>
    <div class="body">
      <p>Lorem ipsum dolor sit amet, consectetuer adipiscing elit, sed diam nonummy nibh euismod tincidunt ut laoreet dolore magna aliquam erat volutpat. Ut wisi enim ad minim veniam, quis nostrud exerci tation ullamcorper suscipit lobortis nisl ut aliquip ex ea commodo consequat. Duis autem vel eum iriure dolor in hendrerit in vulputate velit esse molestie.</p>
      <p>Consequat, vel illum dolore eu feugiat nulla facilisis at vero eros et accumsan et iusto odio dignissim qui blandit praesent luptatum zzril delenit augue duis dolore te feugait nulla facilisi.</p>
      <p>Lorem ipsum dolor sit amet, consectetuer adipiscing elit, sed diam nonummy nibh.</p>
    </div>
  </div>
  <div class="brand-tag"><span class="mark"></span>Ardenholt</div>
  <div class="tc-box">
    <div class="s-title">Lorem ipsum<br>dolor sit</div>
    <div class="s-rule"></div>
    <div class="body">
      <p>Lorem ipsum dolor sit amet, consectetuer adipiscing elit, sed diam nonummy nibh euismod tincidunt ut laoreet dolore magna aliquam erat volutpat. Ut wisi enim ad minim veniam, quis nostrud exerci tation ullamcorper suscipit lobortis nisl ut aliquip ex ea commodo consequat. Duis autem vel eum iriure dolor in hendrerit in vulputate velit esse molestie.</p>
      <p>Consequat, vel illum dolore eu feugiat nulla facilisis at vero eros et accumsan et iusto odio dignissim qui blandit praesent luptatum zzril delenit augue duis dolore te feugait nulla facilisi.</p>
    </div>
  </div>
  <div class="base-line" style="left:115px;width:112px"></div><div class="page-no">4</div>
</article>

<article class="slide col2 row2">
  <div class="s-title" style="left:14px;top:12px">Lorem ipsum dolor sit</div>
  <div class="s-rule" style="left:14px;top:28px"></div>
  <div class="brand-tag"><span class="mark"></span>Ardenholt</div>
  <div class="base-line"></div><div class="page-no">5</div>
</article>

<article class="slide col3 row2">
  <div class="brand-tag"><span class="mark"></span>Ardenholt</div>
  <div class="base-line"></div><div class="page-no">6</div>
</article>

<article class="slide col1 row3 cc">
  <div class="photo cc-photo" role="img" aria-label="Soft faded photo of a bright apartment interior"></div>
  <div class="brand-tag"><span class="mark"></span>Ardenholt</div>
  <div class="num" style="top:32px">1°</div>
  <div class="s-title" style="top:33px">Lorem ipsum dolor sit</div>
  <div class="body" style="top:44px">
    <p>Lorem ipsum dolor sit amet, consectetuer adipiscing elit, sed diam nonummy nibh euismod tincidunt ut laoreet dolore magna aliquam erat volutpat. Ut wisi enim ad minim veniam, quis nostrud exerci tation ullamcorper suscipit lobortis nisl ut aliquip ex ea commodo consequat. Duis autem vel eum iriure dolor in hendrerit in vulputate velit esse molestie.</p>
    <p>Consequat, vel illum dolore eu feugiat nulla facilisis at vero eros et accumsan et iusto odio dignissim qui blandit praesent luptatum zzril delenit augue duis dolore te feugait nulla facilisi.</p>
  </div>
  <div class="num" style="top:98px">2°</div>
  <div class="s-title" style="top:98px">Lorem ipsum dolor sit</div>
  <div class="body" style="top:109px">
    <p>Lorem ipsum dolor sit amet, consectetuer adipiscing elit, sed diam nonummy nibh euismod tincidunt ut laoreet dolore magna aliquam erat volutpat. Ut wisi enim ad minim veniam, quis nostrud exerci tation ullamcorper suscipit lobortis nisl ut aliquip ex ea commodo consequat. Duis autem vel eum iriure dolor in hendrerit in vulputate velit esse molestie.</p>
    <p>Consequat, vel illum dolore eu feugiat nulla facilisis at vero eros et accumsan et iusto odio dignissim qui blandit praesent luptatum zzril delenit augue duis dolore te feugait nulla facilisi.</p>
  </div>
  <div class="base-line"></div><div class="page-no">7</div>
</article>

<article class="slide col2 row3 pc">
  <div class="pc-panel"></div>
  <div class="s-title" style="left:14px;top:32px">Lorem ipsum dolor sit</div>
  <div class="photo pc-photo" role="img" aria-label="Photo of a residential apartment block with trees"></div>
  <div class="brand-tag light"><span class="mark"></span>Ardenholt</div>
  <div class="body">
    <p>Lorem ipsum dolor sit amet, consectetuer adipiscing elit, sed diam nonummy nibh euismod tincidunt ut laoreet dolore magna aliquam erat volutpat. Ut wisi enim ad minim veniam, quis nostrud exerci tation ullamcorper suscipit lobortis nisl ut aliquip ex ea commodo consequat. Duis autem vel eum iriure dolor in hendrerit in vulputate.</p>
    <p>Consequat, vel illum dolore eu feugiat nulla facilisis at vero eros et accumsan et iusto odio dignissim qui blandit praesent luptatum zzril delenit augue.</p>
    <p>Lorem ipsum dolor sit amet, consectetuer adipiscing elit, sed diam nonummy nibh euismod tincidunt ut laoreet dolore magna aliquam erat volutpat.</p>
  </div>
  <div class="base-line"></div><div class="page-no" style="color:#fff">8</div>
</article>

<article class="slide col3 row3 pg">
  <div class="photo tile" style="left:0;top:0;height:54px" role="img" aria-label="Photo of an apartment building facade"></div>
  <div class="tile" style="left:55px;top:0;height:57px;background:var(--beige)"></div>
  <div class="tile" style="left:0;top:57px;height:57px;background:var(--beige)"></div>
  <div class="photo tile" style="left:55px;top:57px;height:57px" role="img" aria-label="Photo of an apartment building corner"></div>
  <div class="photo tile" style="left:0;top:114px;height:56px;background:linear-gradient(180deg,#dfe4e6,#b9b2a6 50%,#4a4a48)" role="img" aria-label="Photo of a light apartment building facade"></div>
  <div class="tile" style="left:55px;top:114px;height:56px;background:var(--orange)"></div>
  <div class="brand-tag"><span class="mark"></span>Ardenholt</div>
  <div class="s-title">Lorem ipsum<br>dolor sit</div>
  <div class="s-rule"></div>
  <div class="body">
    <p>Lorem ipsum dolor sit amet, consectetuer adipiscing elit, sed diam nonummy nibh euismod tincidunt ut laoreet dolore magna aliquam erat volutpat. Ut wisi enim ad minim veniam, quis nostrud exerci tation ullamcorper suscipit lobortis nisl ut aliquip ex ea commodo consequat.</p>
    <p>Consequat, vel illum dolore eu feugiat nulla facilisis at vero eros et accumsan et iusto odio dignissim qui blandit praesent luptatum zzril delenit augue duis dolore te feugait nulla facilisi.</p>
    <p>Lorem ipsum dolor sit amet, consectetuer adipiscing elit, sed diam nonummy nibh euismod tincidunt ut laoreet dolore magna aliquam erat volutpat. Ut wisi enim ad minim veniam, quis nostrud exerci tation ullamcorper. Lorem ipsum dolor sit amet, consectetuer adipiscing elit, sed diam nonummy nibh euismod tincidunt.</p>
  </div>
  <div class="base-line" style="left:109px;width:119px"></div><div class="page-no">9</div>
</article>

<article class="slide col1 row4">
  <div class="photo ty-photo" role="img" aria-label="Photo of a modern brick apartment building"></div>
  <div class="ty-strip"></div>
  <div class="ty-card">
    <div class="big">THANK YOU</div>
    <div class="rule"></div>
    <div class="name">Ardenholt</div>
  </div>
  <div class="page-no">11</div>
</article>

</body>
</html>
```